Larkfield Financial Plans

I am looking for a complete resdesign of my small financial presentation. This is a Word Doc/PDF that I print off when meeting with people in private. I often present my "two pager" that I have been using for years and years. It tells them the basics of what I do, how I help people and foundational financial principles.

I have recently gone out on my own in business and have completely rebranded. This presentation is my most used tool, so it is the first of many things I would like to redo. I am hoping it will somehow coordinate with the colors of my business, not necessarily the EXACT same 3 colors everywhere, but have the design colors compliment.

I've uploaded all my logo designs, as well as the current "two-pager". I am not against it going to 3 pages if needed. As it will still land on 2 pages with duplex printing.

It has always been VERY simple. I am wanting it built into a more professional and design specific format, to show off my branding, without being over cluttered.

I am completely open to ANY graphics changes. Obviously some are very novice, the house on the last page has always been overly simplified.

```html
<!DOCTYPE html>
<html lang="en">
<head>
<meta charset="UTF-8">
<title>Larkfield Financial Plans – The Financial Challenge</title>
<link href="https://fonts.googleapis.com/css2?family=Montserrat:wght@600;700;800;900&family=Raleway:wght@400;500;700&display=swap" rel="stylesheet">
<style>
:root{
  --bg:#8aa9d4;
  --mint:#e3f5ea;
  --green:#1eb53a;
  --navy:#0d1f33;
  --ink:#1b1f24;
  --body:#3c4148;
  --muted:#666c74;
  --blue:#1565c0;
  --line:#c9d3cc;
  --red:#e3191b;
  --panel:#f3f5f4;
}
*{box-sizing:border-box;margin:0;padding:0}
html,body{width:1200px;height:593px;overflow:hidden}
body{background:var(--bg);position:relative;font-family:'Raleway',sans-serif;color:var(--body)}
.page{position:absolute;top:41px;width:362px;height:512px;background:linear-gradient(160deg,#fff 30%,var(--mint) 100%);overflow:hidden;box-shadow:0 4px 14px rgba(20,40,80,.18)}
.page-one{left:42px}
.page-two{left:419px}
.page-three{left:796px}
.abs{position:absolute}
.h-head{font-family:'Montserrat',sans-serif;font-weight:900;color:var(--ink);line-height:.95;letter-spacing:-.5px}
.green{color:var(--green)}

/* page one */
.trend-art{left:186px;top:10px;width:172px;height:196px;border-radius:10px;background:linear-gradient(200deg,rgba(60,220,160,.35) 0%,rgba(21,101,192,.18) 60%,rgba(255,255,255,0) 100%)}
.brand{left:28px;top:36px;font-family:'Montserrat',sans-serif;font-weight:700;font-size:12.5px;color:var(--navy)}
.title-the{left:28px;top:80px;font-size:31px}
.title-fin{left:28px;top:108px;font-size:31px}
.title-band{left:29px;top:136px;width:213px;height:42px;background:var(--green);transform:rotate(-2deg);color:#fff;font-family:'Montserrat',sans-serif;font-weight:900;font-size:29px;display:flex;align-items:center;justify-content:center;letter-spacing:-.5px}
.stat-box{top:194px;width:151px;height:176px;border:1px solid var(--line);background:rgba(255,255,255,.7);padding:10px 8px 0}
.stat-box h3,.insurance h3{font-family:'Montserrat',sans-serif;font-weight:800;font-size:12px;color:var(--navy);margin-bottom:6px}
.stat-box.debt h3{color:var(--green)}
.checks{list-style:none}
.checks li{position:relative;padding-left:13px;font-size:8.2px;line-height:1.27;margin-bottom:7px}
.checks li::before{content:"";position:absolute;left:1px;top:2px;width:6px;height:3px;border-left:1px solid var(--ink);border-bottom:1px solid var(--ink);transform:rotate(-45deg)}
.checks b{color:var(--ink);font-weight:700}
.insurance{left:33px;top:393px;width:300px}

/* page two */
.challenge-panel{left:15px;top:15px;width:331px;height:277px;background:var(--panel);border:1px solid #b8dcc0}
.sec-title{font-size:17px}
.step{width:90px;text-align:center;font-size:6.8px;line-height:1.25;color:var(--muted)}
.step .icon{width:26px;height:26px;margin:0 auto 4px;border-radius:50%;background:linear-gradient(135deg,#d9e4dc,#bfd0c4)}
.step h4{font-family:'Montserrat',sans-serif;font-weight:800;font-size:7.6px;line-height:1;color:var(--ink);margin-bottom:6px}
.step h4.green{color:var(--green)}
.step .em{color:var(--ink);font-size:7.4px;font-weight:500}
.photo-cash{left:287px;top:211px;width:75px;height:117px;border-radius:6px 6px 20px 20px;background:linear-gradient(180deg,#9bae8c 0%,#c9d1c0 45%,#f1f2f0 55%,#e2e4e3 100%)}
.pie-label{font-size:7.4px;color:var(--ink);line-height:.95}
.pie-savings{font-family:'Montserrat',sans-serif;font-weight:700;font-size:8.5px;color:var(--ink)}
.goals{left:203px;top:335px;width:150px;font-size:7.4px;color:var(--ink);display:grid;grid-template-columns:65px 80px;row-gap:4px;line-height:1.1}
.goals span{position:relative;padding-left:10px}
.goals span::before{content:"";position:absolute;left:0;top:1px;width:5px;height:5px;border:1px solid var(--ink)}
.partners{left:202px;top:390px;width:143px;height:100px;background:#fff;border:1px solid var(--line);display:grid;grid-template-columns:1fr 1fr;padding:8px 7px;gap:4px 4px;align-content:space-around}
.partners span{font-family:'Montserrat',sans-serif;font-weight:700;font-size:6.3px;color:var(--navy);display:flex;align-items:center;gap:3px}
.partners span::before{content:"";width:5px;height:5px;border-radius:50%;background:var(--blue)}

/* page three */
.rule-band{left:0;top:0;width:362px;height:247px;background:var(--navy)}
.rule-title{left:34px;top:34px;font-size:17px;color:#fff}
.rate{color:#fff}
.rate .pct{position:absolute;left:0;top:0;font-family:'Montserrat',sans-serif;font-weight:900;font-size:17px;color:var(--green)}
.rate .note{position:absolute;left:35px;top:1px;font-family:'Montserrat',sans-serif;font-weight:700;font-size:6.4px;line-height:1.2;white-space:nowrap}
.rate ul{position:absolute;top:19px;list-style:none;font-size:8.2px;line-height:1.5;white-space:nowrap}
.rate li::before{content:"› ";font-weight:700;margin-right:3px}
.rate-divider{left:142px;width:1px;background:#41566c}
.photo-piggy{left:243px;top:15px;width:108px;height:112px;border-radius:14px;background:linear-gradient(150deg,#1f7a3a 0%,#f3b3b6 40%,#e8a3a6 65%,#b88a4a 100%)}
.structure-title{left:0;width:362px;top:271px;text-align:center;font-size:17px;color:var(--green)}
.pill{top:301px;width:119px;height:30px;border-radius:15px;background:#fff;box-shadow:0 2px 5px rgba(0,0,0,.12);text-align:center;font-family:'Montserrat',sans-serif;font-weight:800;font-size:6.6px;line-height:1.1;padding-top:8px;color:var(--ink)}
.pill .g{color:var(--green)}
.card{top:358px;width:71px;height:128px;background:#fff;border:1px solid var(--line);text-align:center;font-size:6.8px;line-height:1.15;color:var(--muted);padding-top:11px}
.card h5{font-family:'Montserrat',sans-serif;font-weight:800;font-size:8.3px;color:var(--ink);margin-bottom:7px}
.card h5.g{color:var(--green)}
.card p{margin-bottom:6px}
.card .tag{position:absolute;left:0;right:0;bottom:9px;font-family:'Montserrat',sans-serif;font-weight:900;font-size:11.5px;color:var(--red);line-height:1}
</style>
</head>
<body>

<!-- PAGE ONE -->
<section class="page page-one">
  <div class="abs trend-art" role="img" aria-label="Illustration of a rising and falling market trend arrow"></div>
  <div class="abs brand">Larkfield Financial Plans</div>
  <div class="abs h-head title-the">THE</div>
  <div class="abs h-head title-fin">FINANCIAL</div>
  <div class="abs title-band">CHALLENGE</div>

  <div class="abs stat-box savings" style="left:26px">
    <h3>SAVINGS</h3>
    <ul class="checks">
      <li><b>49%</b> of Canadian employees are living pay-cheque to pay cheque. 25% of Canadians are unable to cover an unexpected $500 expense-StatNorth (Feb, 2023)</li>
      <li><b>25%</b> of Canadians need to access their retirement savings early. <b>20%</b> of Canadians have no savings. <b>39%</b> of Canadians aged 55-65 have less than <b>$5,000</b> in savings.</li>
    </ul>
  </div>
  <div class="abs stat-box debt" style="left:184px">
    <h3>DEBT</h3>
    <ul class="checks">
      <li>The average Canadian has <b>$22,131</b> in consumer debt. Which excludes mortgages. Creditline Data (Aug. 2024)</li>
      <li>Over <b>55%</b> of Canadians hold credit card debt and the total Canadian household debt has increased to <b>$2.52</b> trillion, including consumer credit, mortgage &amp; non-mortgage loans. National Lenders Assoc. (Aug. 2024)</li>
    </ul>
  </div>

  <div class="abs insurance">
    <h3>INSURANCE</h3>
    <ul class="checks">
      <li><b>49%</b> of Canadians do not have individual life insurance coverage, but <b>48%</b> say their families would face financial trouble within 6 months of losing someone. Lifeview Research (apr. 2023)</li>
      <li>2-in-5 Canadians (<b>43%</b> women | <b>44%</b> men) will be diagosed with a form ofcancer or other critical illness during their lifetime. Every 7 seconds. Wellstat Canada (June 2024)</li>
    </ul>
  </div>
</section>

<!-- PAGE TWO -->
<section class="page page-two">
  <div class="abs challenge-panel"></div>
  <div class="abs h-head sec-title" style="left:34px;top:34px">FACING THE<br><span class="green">CHALLENGE</span></div>

  <svg class="abs" style="left:0;top:0" width="362" height="512" viewBox="0 0 362 512" aria-hidden="true">
    <g fill="none" stroke="#1b1f24" stroke-width=".9" stroke-dasharray="3 2">
      <path d="M90,104 Q105,116 124,104"/>
      <path d="M192,104 Q208,90 226,102"/>
      <path d="M290,138 Q300,155 290,174"/>
      <path d="M238,210 Q230,228 208,222"/>
      <path d="M126,214 Q112,200 92,216"/>
    </g>
    <g fill="#1b1f24">
      <polygon points="124,100 127,106 121,106"/>
      <polygon points="226,98 229,104 223,104"/>
      <polygon points="287,172 293,172 290,178"/>
      <polygon points="208,219 208,225 203,222"/>
      <polygon points="92,213 92,219 87,217"/>
    </g>
  </svg>

  <div class="abs step" style="left:19px;top:80px"><div class="icon" role="img" aria-label="Money bag and coins icon"></div><h4>CASH<br>FLOW</h4>Analyze<br><br><span class="em">Free-Up</span><br>400% - 600%</div>
  <div class="abs step" style="left:115px;top:80px"><div class="icon" role="img" aria-label="Umbrella over money icon"></div><h4 class="green">CASH FLOW<br>PROTECTIN</h4>Income Protection<br><br>Life Insurance | CI &amp;<br>DI Insurance</div>
  <div class="abs step" style="left:215px;top:80px"><div class="icon" role="img" aria-label="Debt chart icon"></div><h4>DEBT<br>MANAGEMENT</h4>20%<br><br>6% - 7%</div>
  <div class="abs step" style="left:218px;top:165px"><div class="icon" role="img" aria-label="Savings jar icon"></div><h4 class="green">EMERGENCY<br>FUNDS</h4><span class="em">Analyze</span><br>If | When<br><br><span class="em">Free-Up</span><br>9 to 6 months</div>
  <div class="abs step" style="left:115px;top:175px"><div class="icon" role="img" aria-label="Gold bars and money bag icon"></div><h4>BUILD<br>WEALTH</h4><span class="em">Financial<br>Independence<br>Number (F.I.N)</span></div>
  <div class="abs step" style="left:16px;top:185px"><div class="icon" role="img" aria-label="Hands holding coin icon"></div><h4 class="green">PRESENT<br>WEALTH</h4><span class="em">Analyze</span><br>Leaving a legacy<br><br><span class="em">Free-Up</span><br>Will Prep</div>

  <div class="abs photo-cash" role="img" aria-label="Photo of banknotes in a white mug"></div>

  <div class="abs h-head sec-title" style="left:34px;top:317px">HOW WE WILL<br><span class="green">DOING IT?</span></div>

  <svg class="abs" style="left:15px;top:355px" width="200" height="150" viewBox="0 0 200 150" aria-hidden="true">
    <g transform="translate(62,68)">
      <path d="M0,0 L-1,-44 A44,44 0 0 0 12,42 Z" fill="#8fe8cf"/>
      <path d="M2,-2 L2,-46 A44,44 0 0 1 34,-30 Z" fill="#74d3ec"/>
      <path d="M8,2 L42,-26 A44,44 0 0 1 48,10 Z" fill="#a8dff0"/>
      <path d="M3,3 L44,12 A44,44 0 0 1 15,44 Z" fill="#84b6f5"/>
    </g>
    <g stroke="#1b1f24" stroke-width=".6" fill="none">
      <path d="M13,33 L13,54 L19,54"/>
      <path d="M70,14 L70,22"/>
      <path d="M110,62 L116,62"/>
      <path d="M86,100 L96,100 L96,104"/>
    </g>
  </svg>
  <div class="abs pie-label" style="left:17px;top:371px">Living<br>Expanses</div>
  <div class="abs pie-label" style="left:80px;top:360px">Debt</div>
  <div class="abs pie-savings" style="left:132px;top:418px">SAVINGS</div>
  <div class="abs pie-label" style="left:111px;top:459px">Taxes</div>

  <svg class="abs" style="left:175px;top:350px" width="30" height="145" viewBox="0 0 30 145" aria-hidden="true">
    <path d="M17,6 L10,6 L10,142 L17,142 M4,72 L10,72" fill="none" stroke="#1b1f24" stroke-width=".7"/>
  </svg>
  <div class="abs goals">
    <span>Retirement Savings</span><span>Proper Protection</span>
    <span>Children's Education</span><span>Freedom from Debt</span>
  </div>

  <div class="abs partners">
    <span>Harborline</span><span>Maplecrest</span>
    <span>Stonebridge Ins.</span><span>Oakvale</span>
    <span>Summit Life</span><span>Ridgeway Ins.</span>
    <span>Cedarpoint</span><span>Vantora</span>
    <span>Northlake Life</span><span>Brightmoor</span>
  </div>
</section>

<!-- PAGE THREE -->
<section class="page page-three">
  <div class="abs rule-band"></div>
  <div class="abs h-head rule-title">RULE OF 72</div>
  <div class="abs photo-piggy" role="img" aria-label="Photo of a pink piggy bank beside stacks of coins"></div>

  <div class="abs rate" style="left:35px;top:66px">
    <span class="pct">4%</span><span class="note">MONEY DOUBLES<br>EVERY 18 YEARS</span>
    <ul style="left:0"><li>Age 29 | $10,000</li><li>Age 47 | $20,000</li><li>Age 65 | $40,000</li></ul>
  </div>
  <div class="abs rate" style="left:154px;top:66px">
    <span class="pct">6%</span><span class="note">MONEY DOUBLES<br>EVERY 12 YEARS</span>
    <ul style="left:0;line-height:1.25"><li>Age 29 | $10,000</li><li>Age 41 | $20,000</li><li>Age 53 | $40,000</li><li>Age 65 | $80,000</li></ul>
  </div>
  <div class="abs rate-divider" style="top:62px;height:110px"></div>

  <div class="abs rate" style="left:35px;top:151px">
    <span class="pct">8%</span><span class="note">MONEY DOUBLES<br>EVERY 9 YEARS</span>
    <ul style="left:0;line-height:1.48"><li>Age 29 | $10,000</li><li>Age 38 | $20,000</li><li>Age 47 | $40,000</li><li>Age 56 | $80,000</li><li>Age 6 | $160,000</li></ul>
  </div>
  <div class="abs rate" style="left:154px;top:151px">
    <span class="pct">12%</span><span class="note" style="left:44px">MONEY DOUBLES<br>EVERY 9 YEARS</span>
    <ul style="left:0;line-height:1.48"><li>Age 29 | $10,000</li><li>Age 35 | $20,000</li><li>Age 41 | $40,000</li><li>Age 47 | $80,000</li></ul>
    <ul style="left:93px;line-height:1.48"><li>Age 53 | $160,000</li><li>Age 59 | $320,000</li><li>Age 65 | $640,000</li></ul>
  </div>
  <div class="abs rate-divider" style="top:150px;height:82px"></div>

  <div class="abs h-head structure-title">STRUCTURE</div>
  <div class="abs pill" style="left:38px"><span class="g">LIFE INSURANCE ILLNESS</span><br>CRITICAL | DISABILITY</div>
  <div class="abs pill" style="left:209px"><span class="g">DEBT MANAGEMENT</span><br>CASH FLOW</div>

  <svg class="abs" style="left:0;top:331px" width="362" height="27" viewBox="0 0 362 27" aria-hidden="true">
    <g fill="none" stroke="#555" stroke-width=".6" stroke-dasharray="1.5 1">
      <path d="M97,0 V12 M57,27 V12 H138 V27"/>
      <path d="M268,0 V12 M228,27 V12 H308 V27"/>
    </g>
  </svg>

  <div class="abs card" style="left:22px"><h5>HOME</h5><p>Partner with Mortgage</p><p>Brokers for best rates</p><p style="margin-top:12px">Mortgage Insurance</p><p>Alternatives</p><span class="tag" style="font-size:9px">SELL</span></div>
  <div class="abs card" style="left:102px"><h5 class="g">RRSP</h5><p>Tax Deduction</p><p>Brokers for best rates</p><span class="tag">100%<br>TAX</span></div>
  <div class="abs card" style="left:193px"><h5>TFSA</h5><p>No Tax Deduction</p><p>Tax Free Growth</p><p>200<br>$95,000</p><p>Limit 2023<br>$7,000 per year</p><span class="tag">0% TAX</span></div>
  <div class="abs card" style="left:273px"><h5 class="g">PERM LIFE</h5><p>No Tax Deduction</p><p>Qualify</p><p>Tax Deferred Growth</p><span class="tag">0% TAX</span></div>
</section>

</body>
</html>
```